Marks of Dunmore business card design

I need a clean, professional looking design using the attached logo with a bright green/ gray/dark gray/black colors. Maybe even an orange accent if it looks good. I am open to slight changes in the logo if needed. Details below on the info on what should be on the cards. We are a sign company in Ft. Lauderdale FL that specializes in yacht lettering on multi million dollar yachts.

Target Market(s)

marine industry, yachts

Industry/Entity Type

Business

Colors
9bcb3c
000000
606060
f37122

Requirements
Must have
• address: 4837 W. Tallow Rd.
• Cedar Cove, GA 31522
• Phone: 555-518-4062
• email/website: marksofdunmore@postvane.com MarksofDunmore.com
Nice to have
• I would like it very clean and simple but professional looking. Nice layout and would prefer a darker background. Orange highlight only if it works.
Should not have
• Nothing fancy.

```html
<!DOCTYPE html>
<html lang="en">
<head>
<meta charset="utf-8">
<title>Marks of Dunmore – Business Card</title>
<link href="https://fonts.googleapis.com/css2?family=Roboto:wght@400;500;700;900&display=swap" rel="stylesheet">
<style>
  :root {
    --backdrop: #5e5e5e;
    --card: #151515;
    --edge: #f37122;
    --green: #0d8a3a;
    --orange: #f37122;
    --ink-light: #e6e6e6;
  }
  html, body {
    margin: 0;
    width: 1200px;
    height: 828px;
    overflow: hidden;
    background: var(--backdrop);
    font-family: "Roboto", sans-serif;
  }
  .canvas {
    width: 1200px;
    height: 828px;
    display: flex;
    align-items: center;
    justify-content: center;
  }
  .card {
    width: 840px;
    height: 480px;
    box-sizing: border-box;
    padding-top: 118px;
    background: var(--card);
    border: 3px solid var(--edge);
    display: flex;
    flex-direction: column;
    align-items: center;
    text-align: center;
    box-shadow: 0 18px 40px rgba(0,0,0,0.35);
  }
  .brand-name {
    margin: 0 0 44px;
    font-weight: 900;
    font-size: 50px;
    line-height: 1;
    letter-spacing: 1px;
    text-transform: uppercase;
    color: var(--green);
  }
  .person-name {
    margin: 0;
    font-weight: 500;
    font-size: 20px;
    line-height: 1.2;
    text-transform: uppercase;
    color: var(--green);
  }
  .person-title {
    margin: 2px 0 16px;
    font-weight: 500;
    font-size: 16px;
    line-height: 1.2;
    text-transform: uppercase;
    color: var(--orange);
  }
  .address {
    margin: 0 0 6px;
    font-size: 16px;
    line-height: 1.3;
    letter-spacing: 0.5px;
    color: var(--ink-light);
  }
  .contact-line {
    display: flex;
    align-items: center;
    gap: 14px;
    font-size: 16px;
    line-height: 1.3;
    letter-spacing: 0.5px;
    color: var(--ink-light);
  }
  .contact-item {
    display: flex;
    align-items: center;
    gap: 6px;
  }
  .contact-icon {
    width: 13px;
    height: 13px;
    fill: var(--green);
  }
</style>
</head>
<body>
<main class="canvas">
  <section class="card">
    <h1 class="brand-name">Marks of Dunmore</h1>
    <p class="person-name">Evan Hale</p>
    <p class="person-title">CEO/Founder</p>
    <p class="address">4837 W. Tallow Rd., Cedar Cove, GA 31522</p>
    <div class="contact-line">
      <span class="contact-item">
        <svg class="contact-icon" viewBox="0 0 24 24" aria-hidden="true"><path d="M6.6 10.8a15.1 15.1 0 0 0 6.6 6.6l2.2-2.2c.3-.3.7-.4 1-.2 1.1.4 2.3.6 3.6.6.6 0 1 .4 1 1V20c0 .6-.4 1-1 1A17 17 0 0 1 3 4c0-.6.4-1 1-1h3.5c.6 0 1 .4 1 1 0 1.3.2 2.5.6 3.6.1.3 0 .7-.2 1z"/></svg>
        555-518-4062
      </span>
      <span class="contact-item">
        <svg class="contact-icon" viewBox="0 0 24 24" aria-hidden="true"><path d="M2 5h20v14H2z"/></svg>
        marksofdunmore@postvane.com
      </span>
      <span class="contact-item">
        <svg class="contact-icon" viewBox="0 0 24 24" aria-hidden="true"><circle cx="12" cy="12" r="10"/></svg>
        www.MarksofDunmore.com
      </span>
    </div>
  </section>
</main>
</body>
</html>
```